Email signature design - law firm

We are a small boutique law firm which is located near the beach in Manly, Australia.

We have just recently developed a new logo and are looking to redesign our letterhead, business cards and email signatures.

This brief is for our email signatures. This is an email signature to appear at the bottom of our Outlook emails so we would like it to be text that we are able to edit as the wording in our email signature often required amendments.

I have attached a word document which had our new logo, and our previous email signature which all the information/wording that needs to be included.

We would like multiple designs with a modern, simplistic yet striking look.

Thanks.

font - raleway or montserrat
Updates

Colors

Designer to choose colors to be used in the design.

Requirements
Must have
• Must have the exact wording which appears in the email signature in the word document attached to brief.
• Must be able to edit the text as it is for an Outlook email signature which wording will change from time to time.

```html
<!DOCTYPE html>
<html lang="en">
<head>
<meta charset="utf-8">
<title>Harwell &amp; Partners – Stationery</title>
<link href="https://fonts.googleapis.com/css2?family=Raleway:wght@800&family=Open+Sans:wght@400&display=swap" rel="stylesheet">
<style>
:root{
  --backdrop:#9b9b9b;
  --paper:#fbfbfb;
  --navy:#1e2f6e;
  --blue-light:#6a7ec0;
  --name-blue:#4f62ad;
  --gold:#b8ab7c;
  --gold-dark:#838063;
  --ink:#222;
  --text:#444;
  --muted:#555;
  --wash:#eceef6;
}
*{margin:0;padding:0;box-sizing:border-box}
html,body{width:939px;height:1200px;overflow:hidden;background:var(--backdrop)}
.stage{position:absolute;left:0;top:0;width:1139px;height:1455px;transform:scale(0.8244);transform-origin:0 0}
.sheet{position:absolute;background:var(--paper);box-shadow:0 0 0 1px #ddd;overflow:hidden}
.business-card{left:207px;top:93px;width:725px;height:189px}
.letterhead{left:207px;top:321px;width:725px;height:1026px}

.header-band{position:absolute;left:0;top:0;width:100%;height:18px;background:linear-gradient(90deg,var(--blue-light),var(--navy));border-bottom:5px solid var(--gold-dark)}

.mark{position:absolute;border-radius:50%;background:var(--navy)}
.firm-name{position:absolute;font-family:'Raleway',sans-serif;font-weight:800;color:var(--ink);letter-spacing:1.6px;white-space:nowrap}
.firm-tag{position:absolute;font-family:'Open Sans',sans-serif;font-weight:400;color:var(--ink);white-space:nowrap}

.business-card .mark{left:30px;top:36px;width:38px;height:38px}
.business-card .firm-name{left:166px;top:35px;font-size:20px}
.business-card .firm-tag{left:216px;top:62px;font-size:11px;letter-spacing:14px}

.person{position:absolute;left:27px;top:126px}
.person-name{font-family:'Raleway',sans-serif;font-weight:800;font-size:19px;color:var(--name-blue)}
.person-role{font-family:'Open Sans',sans-serif;font-size:11px;color:var(--muted);margin-top:1px}

.contact{position:absolute;list-style:none;font-family:'Open Sans',sans-serif;font-size:13px;color:var(--text)}
.contact li{height:19.3px;display:flex;align-items:center;white-space:nowrap}
.icon{width:11px;height:11px;fill:var(--name-blue);flex:none}
.business-card .contact{right:50px;top:67px}
.business-card .contact li{justify-content:flex-end}
.business-card .contact .icon{margin-left:9px}
.business-card .address{position:absolute;right:51px;top:147px;font-family:'Open Sans',sans-serif;font-size:13.5px;color:var(--text);white-space:nowrap}

.letterhead .mark{left:126px;top:52px;width:44px;height:44px}
.letterhead .firm-name{left:148px;top:128px;font-size:14px;transform:translateX(-50%)}
.letterhead .firm-tag{left:150px;top:149px;font-size:8px;letter-spacing:9px;transform:translateX(-50%)}
.letterhead .contact{left:433px;top:82px}
.letterhead .contact .icon{margin-right:15px}

.watermark-area{position:absolute;left:62px;top:395px;width:600px;height:260px;border-radius:130px;background:radial-gradient(ellipse at center,var(--wash) 0%,rgba(236,238,246,0) 70%)}

.footer-band{position:absolute;left:0;bottom:0;width:100%;height:100px;background:linear-gradient(90deg,var(--blue-light),var(--navy));border-top:6px solid var(--gold)}
.footer-address{position:absolute;left:372px;width:300px;top:966px;text-align:center;color:#fff;font-family:'Open Sans',sans-serif;font-size:13.5px;line-height:19px;white-space:nowrap}
</style>
</head>
<body>
<svg width="0" height="0" style="position:absolute" aria-hidden="true">
  <defs>
    <symbol id="i-phone" viewBox="0 0 12 12"><path d="M1 4c0-2 10-2 10 0v1H8V4H4v1H1z M3 6h6l1.5 4.5h-9z"/></symbol>
    <symbol id="i-mail" viewBox="0 0 12 12"><path d="M1 2.5h10v7H1z M1.8 3.2 6 6.6l4.2-3.4v.9L6 7.5 1.8 4.1z" fill-rule="evenodd"/></symbol>
    <symbol id="i-web" viewBox="0 0 12 12"><circle cx="6" cy="6" r="5"/><path d="M1 6h10M6 1v10M2.5 3.5h7M2.5 8.5h7" stroke="#fff" stroke-width=".7"/></symbol>
  </defs>
</svg>

<main class="stage">
  <section class="sheet business-card" aria-label="Business card">
    <div class="header-band" role="img" aria-label="Decorative navy and gold header band"></div>
    <span class="mark" aria-hidden="true"></span>
    <span class="firm-name">Harwell &amp; Partners</span>
    <span class="firm-tag">LAWYERS</span>
    <div class="person">
      <p class="person-name">Nora Ellison</p>
      <p class="person-role">Managing Director</p>
    </div>
    <ul class="contact">
      <li>(02) 5550 1842<svg class="icon"><use href="#i-phone"/></svg></li>
      <li>(02) 5550 1843<svg class="icon"><use href="#i-phone"/></svg></li>
      <li>nora.ellison@harwelllaw.com.au<svg class="icon"><use href="#i-mail"/></svg></li>
      <li>www.harwellandpartners.com.au<svg class="icon"><use href="#i-web"/></svg></li>
    </ul>
    <p class="address">Suite 4, 12 Coral Lane Seaview NSW 2999</p>
  </section>

  <section class="sheet letterhead" aria-label="Letterhead">
    <div class="header-band" role="img" aria-label="Decorative navy and gold header band"></div>
    <span class="mark" aria-hidden="true"></span>
    <span class="firm-name">Harwell &amp; Partners</span>
    <span class="firm-tag">LAWYERS</span>
    <ul class="contact">
      <li><svg class="icon"><use href="#i-phone"/></svg>(02) 5550 1842</li>
      <li><svg class="icon"><use href="#i-phone"/></svg>(02) 5550 1843</li>
      <li><svg class="icon"><use href="#i-mail"/></svg>nora.ellison@harwelllaw.com.au</li>
      <li><svg class="icon"><use href="#i-web"/></svg>www.harwellandpartners.com.au</li>
    </ul>
    <div class="watermark-area" role="img" aria-label="Faint decorative wave watermark"></div>
    <div class="footer-band" role="img" aria-label="Decorative navy and gold footer band"></div>
    <div class="footer-address">
      <p>Suite 4, 12 Coral Lane</p>
      <p>Seaview NSW 2999</p>
    </div>
  </section>
</main>
</body>
</html>
```